Buch-/E-Book-Cover Existenzgründer und Gründungsinteressierte
Tolles Design, professioneller Ablauf, absolut kundenfreundlicher Service!
Zielgruppe
Es geht um eine Buchcover mit dem Titel 'Nebenbetrieb gründen'; Zielgruppe sind Existenzgründer und Gründungsinteressierte
Aufgabenstellung
Das Buchcover sollte modern und frisch gestaltet werden, eine grobe Skizze ist beigefügt, unten rechts soll das Verlagslogo (klein) platziert werden
Haupttext „Nebenbetrieb gründen“ soll auffallend, vielleicht als Wortmarke, gestaltet werden – er sollte einen Wiedererkennungswert haben
Auf der Frontseite des Covers sollten auch die Schlüsselwörter zu den Hauptkapiteln integriert werden (siehe Idee Skizze), damit der Leser auf den 1. Blick einen Eindruck über die Inhalte des Ratgebers gewinnt
Format: Das Taschenbuch soll im Hochformat (13,97 cm x 21,59 cm, Bindung links, Velloro Print Direct Service) erscheinen und das Buch hat ca. 190 Seiten. Das Cover soll ein Softcover (235g Chromokarton), 4/4 farbig sein.

```html
<!DOCTYPE html>
<html lang="de">
<head>
<meta charset="utf-8">
<title>Nebenbetrieb gründen – Buchcover</title>
<link rel="stylesheet" href="https://fonts.googleapis.com/css2?family=Fira+Sans+Condensed:wght@300;400;600;700;800&display=swap">
<style>
  :root {
    --cover-green: #a2bf38;
    --headline-white: #ffffff;
    --subtitle-green: #587a3c;
    --list-green: #4f7d33;
    --author-yellow: #ffe500;
    --accent-red: #c8102e;
    --band-light: #e6e6e6;
    --band-dark: #b9b9b9;
    --page-bg: #ffffff;
  }
  html, body {
    margin: 0;
    width: 1200px;
    height: 1200px;
    overflow: hidden;
    background: var(--page-bg);
  }
  .stage {
    position: relative;
    width: 1200px;
    height: 1200px;
  }
  .book-cover {
    position: absolute;
    left: 237px;
    top: 40px;
    width: 726px;
    height: 1120px;
    box-shadow: 6px 8px 14px rgba(0,0,0,0.25);
    font-family: "Fira Sans Condensed", "Arial Narrow", sans-serif;
  }
  .book-cover svg { display: block; width: 100%; height: 100%; }
  .title-line { fill: var(--headline-white); font-weight: 800; }
  .title-sub { fill: var(--headline-white); font-weight: 700; }
  .author-name { fill: var(--accent-red); font-weight: 600; }
  .subtitle { fill: var(--subtitle-green); font-weight: 700; }
  .topics-lead { fill: var(--list-green); font-weight: 600; }
  .topic { fill: var(--list-green); font-weight: 300; }
  .bonus-head { fill: var(--accent-red); font-weight: 700; }
  .bonus-text { fill: #111; font-weight: 600; }
  .publisher-name { fill: var(--headline-white); font-weight: 700; }
</style>
</head>
<body>
<main class="stage">
  <div class="book-cover">
    <svg viewBox="0 0 792 1221" xmlns="http://www.w3.org/2000/svg">
      <defs>
        <linearGradient id="photo-tones" x1="0" y1="0" x2="1" y2="0">
          <stop offset="0" stop-color="#ffffff"/>
          <stop offset="0.35" stop-color="#f3f1ee"/>
          <stop offset="0.6" stop-color="#d9cbbd"/>
          <stop offset="0.8" stop-color="#9c7a62"/>
          <stop offset="1" stop-color="#7d93b5"/>
        </linearGradient>
        <linearGradient id="band-shade" x1="0" y1="0" x2="0" y2="1">
          <stop offset="0" stop-color="var(--band-light)"/>
          <stop offset="1" stop-color="var(--band-dark)"/>
        </linearGradient>
      </defs>

      <rect class="cover-base" width="792" height="1221" fill="var(--cover-green)"/>

      <g role="img" aria-label="Foto: lächelnde Ladeninhaberin mit Jeansschürze vor einem Blumengeschäft, links weich ins Weiße ausgeblendet">
        <polygon points="0,553 792,383 792,921 0,1086" fill="url(#photo-tones)"/>
      </g>

      <polygon class="band-upper" points="0,528 792,358 792,383 0,553" fill="url(#band-shade)"/>
      <polygon class="band-lower" points="0,1086 792,921 792,944 0,1109" fill="url(#band-shade)"/>

      <text class="title-line" x="48" y="174" font-size="200" textLength="420" lengthAdjust="spacingAndGlyphs">NEBEN</text>
      <text class="title-line" x="44" y="339" font-size="200" textLength="706" lengthAdjust="spacingAndGlyphs">BETRIEB</text>
      <text class="title-sub" x="47" y="421" font-size="80" textLength="340" lengthAdjust="spacingAndGlyphs">GRÜNDEN</text>

      <rect class="author-box" x="490" y="127" width="258" height="47" fill="var(--author-yellow)"/>
      <text class="author-name" x="619" y="163" font-size="34" text-anchor="middle">Henrik Weidmann</text>

      <text class="subtitle" x="47" y="640" font-size="47">Existenzgründung für</text>
      <text class="subtitle" x="47" y="693" font-size="47">Kleinunternehmen</text>

      <text class="topics-lead" x="52" y="755" font-size="31">Alles über</text>
      <g class="topic-list" font-size="26">
        <text class="topic" x="45" y="803">•  Behördengänge</text>
        <text class="topic" x="45" y="841">•  Rechtsform (digitale) Büroorganisation</text>
        <text class="topic" x="45" y="879">•  Buchhaltung und Steuern</text>
        <text class="topic" x="45" y="917">•  Finanzierung und Fördermittel</text>
        <text class="topic" x="45" y="955">•  Businessplan</text>
        <text class="topic" x="45" y="993">•  Versicherungen</text>
      </g>

      <g class="bonus-badge" transform="translate(334 1034) rotate(-12)">
        <circle r="74" fill="var(--author-yellow)" stroke="var(--accent-red)" stroke-width="7"/>
        <text class="bonus-head" x="-6" y="-20" font-size="28" text-anchor="middle">Bonus</text>
        <text class="bonus-text" x="0" y="8" font-size="19" text-anchor="middle">Online-Trainings</text>
        <text class="bonus-text" x="0" y="32" font-size="19" text-anchor="middle">und Vorlagen</text>
      </g>

      <g class="publisher-mark">
        <rect x="620" y="1040" width="26" height="26" fill="var(--author-yellow)"/>
        <text class="publisher-name" x="654" y="1063" font-size="30">Zahlenfroh</text>
        <text class="publisher-name" x="654" y="1097" font-size="30">Verlag</text>
      </g>
    </svg>
  </div>
</main>
</body>
</html>
```